Young Balance Support Network

We need a poster explaining that some children live with a disability called Vestibular Disorder. Feel free to ask question. We want you to respect our color code, same as our logo.

Here is our website : http://www.ybsnetwork.org/

We need to sensibilise people about this disability for children.

Industry/Entity Type

Charity

Font styles to use
Serif

Requirements
Must have
• 1. our logo (with all our details) + one of the photo of Marek
• 2. design showing a child with a dizziness for exemple
• 3. a title saying : Aidez-nous à changer la vie des enfants vivant avec un problème vestibulaire
• 4.include the text attached (information flyer YBSN)
• Poster size : 24"X 36"
Should not have
• wheel chair

```html
<!DOCTYPE html>
<html lang="fr">
<head>
<meta charset="utf-8">
<title>Young Balance Support Network – Poster</title>
<link href="https://fonts.googleapis.com/css2?family=Fredoka:wght@600&family=Varela+Round&display=swap" rel="stylesheet">
<style>
  :root {
    --sky-top: #8fcdf0;
    --sky-low: #e6f4fb;
    --field: #7fb83a;
    --field-dark: #4f8a26;
    --lime: #c2d62e;
    --blue: #4cb8e8;
    --orange: #f6a623;
    --ink: #2e2e2e;
    --grey: #7a7a7a;
    --white: #ffffff;
    --photo-skin: #f1c9a8;
    --photo-blue: #5a8fd6;
  }
  * { margin: 0; padding: 0; box-sizing: border-box; }
  html, body { width: 800px; height: 1200px; overflow: hidden; background: var(--white); }
  .poster {
    position: relative; width: 800px; height: 1200px; overflow: hidden;
    font-family: "Varela Round", "Helvetica", sans-serif; color: var(--ink);
  }
  .scenery {
    position: absolute; left: 0; top: 0; width: 800px; height: 660px;
    background: linear-gradient(180deg, var(--sky-top) 0%, var(--sky-low) 42%, #a9d46a 60%, var(--field) 78%, var(--field-dark) 100%);
  }
  .child-photo {
    position: absolute; left: 430px; top: 0; width: 370px; height: 485px;
    background: radial-gradient(ellipse at 45% 45%, var(--photo-skin) 0%, #e7b793 45%, rgba(231,183,147,0) 70%),
                linear-gradient(180deg, rgba(255,255,255,0) 60%, var(--photo-blue) 100%);
  }
  .brand { position: absolute; left: 40px; top: 34px; display: flex; flex-direction: column; align-items: center; width: 110px; }
  .brand-mark { width: 70px; height: 70px; border-radius: 50%; background: var(--blue); }
  .brand-name { margin-top: 20px; font-size: 26px; color: var(--lime); letter-spacing: 3px; }
  .account { position: absolute; left: 180px; top: 143px; font-size: 18px; color: var(--grey); }
  .title-band { position: absolute; left: 0; top: 176px; width: 470px; height: 310px; }
  .title {
    position: absolute; left: 28px; top: 190px; width: 420px;
    font-size: 29px; line-height: 33px; color: var(--white);
  }
  .contacts { position: absolute; left: 0; top: 305px; list-style: none; }
  .contacts li {
    display: flex; align-items: center; width: 348px; height: 40px; margin-bottom: 10px;
    background: var(--blue); border-radius: 0 22px 22px 0; padding-left: 30px;
    font-size: 19px; color: var(--ink);
    box-shadow: 2px 2px 4px rgba(0,0,0,.18);
  }
  .contacts svg { width: 28px; height: 28px; margin-right: 18px; flex: none; }
  .social { position: absolute; left: 348px; top: 485px; width: 452px; }
  .social-head {
    height: 38px; background: var(--orange); border-radius: 20px 0 0 0;
    color: var(--white); font-size: 22px; font-style: italic; text-align: center; line-height: 38px;
    font-family: "Fredoka", sans-serif; letter-spacing: 1px;
  }
  .social-list {
    list-style: none; background: var(--white); height: 108px; border-radius: 0 0 0 20px;
    padding: 12px 0 0 30px;
  }
  .social-list li { display: flex; align-items: center; height: 46px; font-size: 18px; color: #444; }
  .social-list .dot { width: 36px; height: 36px; border-radius: 50%; margin-right: 12px; flex: none; }
  .dot-fb { background: #3b5a9a; }
  .dot-tw { background: var(--blue); }
  .info { position: absolute; left: 0; top: 648px; width: 800px; }
  .info-heading {
    height: 39px; border-radius: 0 22px 22px 0; padding-left: 30px;
    font-family: "Fredoka", sans-serif; font-size: 21px; line-height: 39px; color: var(--white);
  }
  .info-heading.blue { background: var(--blue); }
  .info-heading.lime { background: var(--lime); }
  .info p { padding: 0 50px 0 36px; font-size: 13.4px; line-height: 17px; color: var(--ink); }
  .info p + p { margin-top: 16px; }
  .info .block { margin: 8px 0 14px; }
</style>
</head>
<body>
<main class="poster">
  <div class="scenery" role="img" aria-label="Ciel bleu nuageux au-dessus d'un pré vert avec des tournesols et des marguerites"></div>
  <div class="child-photo" role="img" aria-label="Photo d'un jeune enfant souriant portant des lunettes bleues"></div>

  <svg class="title-band" viewBox="0 0 470 310" aria-hidden="true">
    <path d="M0 0 H440 Q470 0 470 30 V60 Q470 130 390 170 Q300 215 0 230 Z" fill="var(--lime)"/>
  </svg>

  <div class="brand">
    <span class="brand-mark" aria-hidden="true"></span>
    <span class="brand-name">YBSN</span>
  </div>
  <p class="account">CCP : 12-345678-9</p>

  <h1 class="title">Aidez-nous à changer la vie des enfants vivant avec un problème vestibulaire</h1>

  <ul class="contacts">
    <li>
      <svg viewBox="0 0 28 28" aria-hidden="true"><g fill="none" stroke="#fff" stroke-width="2"><circle cx="14" cy="14" r="11"/><ellipse cx="14" cy="14" rx="5" ry="11"/><line x1="3" y1="14" x2="25" y2="14"/></g></svg>
      www.ybsnetwork.org
    </li>
    <li>
      <svg viewBox="0 0 28 28" aria-hidden="true"><g fill="none" stroke="#fff" stroke-width="2"><rect x="3" y="7" width="22" height="15"/><polyline points="3,7 14,16 25,7"/></g></svg>
      info@ybsnetwork.org
    </li>
    <li>
      <svg viewBox="0 0 28 28" aria-hidden="true"><path d="M14 3a8 8 0 0 0-8 8c0 6 8 14 8 14s8-8 8-14a8 8 0 0 0-8-8z" fill="#fff"/><circle cx="14" cy="11" r="3" fill="var(--blue)"/></svg>
      Switzerland
    </li>
  </ul>

  <section class="social">
    <h2 class="social-head">PLEASE FIND US ON</h2>
    <ul class="social-list">
      <li><span class="dot dot-fb" aria-hidden="true"></span>@YoungBalanceSupportNetwork</li>
      <li><span class="dot dot-tw" aria-hidden="true"></span>@YBSNetwork</li>
    </ul>
  </section>

  <section class="info">
    <h2 class="info-heading blue" style="width:545px">QU'EST-CE QUE LE VESTIBULE ?</h2>
    <div class="block">
      <p>C’est un organe sensoriel, pilier de votre équilibre, véritable 6ème sens situé dans l’oreille interne.</p>
    </div>

    <h2 class="info-heading lime" style="width:595px">QU'EST CE QU'UNE ARÉFLEXIE VESTIBULAIRE ?</h2>
    <div class="block">
      <p>C’est l’absence complète de toute information vestibulaire. L’enfant a ainsi l’impression que tout vacille autour de lui, jour et nuit.</p>
    </div>

    <h2 class="info-heading blue" style="width:708px">QUELLES EN SONT LES CONSÉQUENCES POUR L'ENFANT ?</h2>
    <div class="block">
      <p>Le développement moteur de l’enfant est retardé car il doit trouver des solutions afin de construire son équilibre, stabiliser son regard et son corps.</p>
      <p>Certains apprentissages sont de véritables obstacles pour l’enfant : se représenter son propre corps, se situer dans l’espace qui l’entoure, interagir avec les autres, communiquer, écrire, lire, manger, boire, marcher. Chacune de ces actions necessitent des efforts considérables pour se concentrer quelques secondes ou minutes.</p>
      <p>Quand l’enfant réussit à effectuer l’une de ces actions, son comportement peut sembler déroutant et bien trop souvent mal interprété par le grand public.</p>
    </div>

    <h2 class="info-heading lime" style="width:565px">QUEL EST LE BUT DE NOTRE ASSOCIATION ?</h2>
    <div class="block">
      <p>Notre association a pour but de promouvoir les troubles vestibulaires chez l’enfant, ses conséquences sur sa santé ainsi que celui de son entourage et de soutenir ces enfants et leurs parents en leur offrant un espace de parole et des solutions concrètes pour soulager leur quotidien. Notre association a également pour but de financer et promouvoir toute action de recherche scientifique visant à aider les enfants ayant un trouble vestibulaire.</p>
    </div>
  </section>
</main>
</body>
</html>
```